Visitenkarten-Design für klassischen Bauernhof
Vielen Dank für die tolle Zusammenarbeit Henrike. Die Visitenkarten sind genau so wie wir sie uns vorgestellt haben. Jederzeit gerne wieder :) LG Ulrike
Liebe Designer,
wir sind ein klassicher Bauernhof mit Ziegen und Direktvermarktung (SB-Hofladen).
Informationen über die Visitenkarten sind unter 'Vorgaben' aufgelistet.
Vielen Dank!
NACHTRAG - VIELEN HERZLICHEN DANK AN ALLE GRAFIKER FÜR DIE UNZÄHLIGEN WIRKLICH RESTLOS TOLLEN DESIGNS!!
DAS WAR KEINE LEICHTE ENTSCHEIDUNG...
Aufgabenstellung
Folgende Angaben sollten auf der Visitenkarte enthalten sein:
Ziegenhof Brunnrieth (Logo)
SB Hofladen täglich geöffnet
Hofkäserei
Die Visitenkarten kann gerne auch beidseitig bedruckt werden.
Eine Zeile um ggf. eine Mobilfunknummer eintragen zu können wäre praktisch aber nicht dringend notwendig (ebenso ein Ziegenbild)

```html
<!DOCTYPE html>
<html lang="de">
<head>
<meta charset="utf-8">
<title>Ziegenhof Brunnrieth – Visitenkarten</title>
<link href="https://fonts.googleapis.com/css2?family=Merriweather:wght@400;700;900&display=swap" rel="stylesheet">
<style>
  :root {
    --brown: #5b2c1a;
    --wood-light: #a8673a;
    --wood-mid: #7a3f22;
    --wood-pale: #d9cfc6;
    --paper: #ffffff;
    --backdrop: #e9e4dc;
  }
  * { box-sizing: border-box; margin: 0; padding: 0; }
  html, body {
    width: 1200px; height: 989px; overflow: hidden;
    background: var(--backdrop);
    font-family: "Merriweather", Georgia, serif;
    color: var(--brown);
  }
  .sheet {
    width: 1200px; height: 989px;
    display: flex; align-items: center; justify-content: center; gap: 60px;
  }
  .card {
    position: relative;
    width: 510px; height: 330px;
    background: var(--paper);
    overflow: hidden;
    box-shadow: 0 2px 6px rgba(0,0,0,.12);
  }
  .card__frame {
    position: absolute; inset: 10px;
    border: 2px solid var(--brown);
    pointer-events: none; z-index: 3;
  }

  /* Kontaktseite */
  .contact { padding: 34px 0 0 40px; position: relative; z-index: 2; }
  .contact__name {
    font-weight: 900; font-size: 19px; letter-spacing: .5px; margin-bottom: 12px;
  }
  .contact__address { font-size: 14px; line-height: 1.35; margin-bottom: 12px; }
  .contact__list { list-style: none; font-size: 14px; line-height: 1.35; }
  .contact__list b { font-weight: 700; display: inline-block; width: 20px; }
  .contact__mobile-line {
    display: inline-block; width: 210px; border-bottom: 1.5px dotted var(--brown);
    vertical-align: -2px;
  }
  .contact__social {
    margin-top: 14px; font-size: 9.5px; display: flex; align-items: center; gap: 5px;
  }
  .contact__social-dot {
    width: 14px; height: 14px; border-radius: 50%; background: var(--brown);
  }
  .photo {
    position: absolute; right: 0; bottom: 0;
    width: 245px; height: 228px; z-index: 1;
    border-top-left-radius: 120% 100%;
    background: linear-gradient(135deg, var(--wood-mid) 0%, var(--wood-light) 40%, var(--wood-pale) 62%, var(--wood-mid) 100%);
  }
  .photo__claim {
    position: absolute; right: 28px; bottom: 26px; z-index: 2;
    color: #fff; text-align: right; font-size: 14px; line-height: 1.3;
  }

  /* Namensseite */
  .brand {
    position: absolute; inset: 0;
    display: flex; align-items: center; justify-content: center;
  }
  .brand__name {
    font-size: 30px; font-weight: 700; color: var(--brown);
    line-height: 1.2; text-align: center;
  }
</style>
</head>
<body>
<main class="sheet">
  <section class="card card--contact">
    <div class="card__frame"></div>
    <div class="contact">
      <h1 class="contact__name">FAMILIE HOLLERBACH</h1>
      <p class="contact__address">Brunnriethweg 4<br>77999 Talbrunn<br>(Post: 77998 Wiesenau-Lindach)</p>
      <ul class="contact__list">
        <li><b>T.</b>07321-614</li>
        <li><b>F.</b>07321-809</li>
        <li><b>M.</b><span class="contact__mobile-line"></span></li>
        <li><b>E.</b>info@ziegenhof-brunnrieth.de</li>
      </ul>
      <p class="contact__social">Besuchen Sie uns auf <span class="contact__social-dot"></span> Hofnetz</p>
    </div>
    <div class="photo" role="img" aria-label="Foto: weiße Ziegen schauen über eine Holzwand im Stall"></div>
    <p class="photo__claim">SB Hofladen<br>Hofkäserei<br>täglich geöffnet!</p>
  </section>

  <section class="card card--brand">
    <div class="card__frame"></div>
    <div class="brand">
      <span class="brand__name">Ziegenhof<br>Brunnrieth</span>
    </div>
  </section>
</main>
</body>
</html>
```